New LLC consulting company needs a business card design

I need a business card design for new company in Alexandria Virginia called TK Verdane Consulting LLC. The company is focused on consulting for defense and national security issues with expertise in nuclear and space topics. I would like to see designs that are simple and I am open to colors except for brown.

Target Market(s)

All businesses that are seeking consulting help

Industry/Entity Type

Consulting

Contact Information for Business Card

Name of company - TK Verdane Consulting LLC; name (Delia Hartwig) President; email: hartwigdl47@mailnest.example; Phone: 555-862-4197

Requirements
Must have
• The details described above
Nice to have
• I'm open to all ideas
Should not have
• No brown

```html
<!DOCTYPE html>
<html lang="en">
<head>
<meta charset="utf-8">
<title>Delia Hartwig – TK Verdane Consulting LLC</title>
<link rel="stylesheet" href="https://fonts.googleapis.com/css2?family=Montserrat:wght@400;700&display=swap">
<style>
  :root {
    --backdrop: #999999;
    --card: #ffffff;
    --ink: #000000;
    --ink-soft: #2b2b2b;
    --rule: #111111;
  }
  * { margin: 0; padding: 0; box-sizing: border-box; }
  html, body {
    width: 1200px;
    height: 1059px;
    overflow: hidden;
    background: var(--backdrop);
    font-family: "Montserrat", sans-serif;
  }
  .business-card {
    position: absolute;
    left: 234px;
    top: 320px;
    width: 732px;
    height: 419px;
    background: var(--card);
    border-radius: 26px;
  }
  .company-name {
    position: absolute;
    left: 37px;
    top: 52px;
    font-size: 17px;
    font-weight: 700;
    line-height: 1;
    color: var(--ink);
    letter-spacing: 1.2px;
    text-transform: uppercase;
  }
  .person-name {
    position: absolute;
    left: 37px;
    top: 138px;
    font-size: 36px;
    font-weight: 700;
    line-height: 1;
    color: var(--ink);
    letter-spacing: 0.2px;
  }
  .person-title {
    position: absolute;
    left: 37px;
    top: 185px;
    font-size: 21px;
    font-weight: 400;
    line-height: 1;
    color: var(--ink-soft);
    letter-spacing: 0.4px;
  }
  .divider {
    position: absolute;
    left: 39px;
    top: 229px;
    width: 655px;
    height: 1.5px;
    background: var(--rule);
  }
  .contact {
    position: absolute;
    top: 251px;
    display: flex;
    align-items: center;
    gap: 10px;
    font-size: 20px;
    line-height: 1;
    color: var(--ink-soft);
    letter-spacing: 0.3px;
    white-space: nowrap;
  }
  .contact-email { left: 39px; }
  .contact-phone { right: 38px; }
  .contact-icon { width: 17px; height: 17px; flex: none; fill: var(--ink); }
</style>
</head>
<body>
  <section class="business-card">
    <p class="company-name">TK Verdane Consulting LLC</p>
    <h1 class="person-name">Delia Hartwig</h1>
    <p class="person-title">President</p>
    <div class="divider"></div>
    <p class="contact contact-email">
      <svg class="contact-icon" viewBox="0 0 16 16" aria-hidden="true">
        <path d="M1 3.5h14v9H1z" fill="var(--ink)"/>
        <path d="M1.5 4.2l6.5 5 6.5-5" fill="none" stroke="#fff" stroke-width="1.1"/>
        <path d="M1.5 12l5-4.2M14.5 12l-5-4.2" fill="none" stroke="#fff" stroke-width="1"/>
      </svg>
      hartwigdl47@mailnest.example
    </p>
    <p class="contact contact-phone">
      <svg class="contact-icon" viewBox="0 0 24 24" aria-hidden="true">
        <path d="M6.6 10.8c1.4 2.8 3.8 5.1 6.6 6.6l2.2-2.2c.3-.3.7-.4 1-.2 1.1.4 2.3.6 3.6.6.6 0 1 .4 1 1V20c0 .6-.4 1-1 1C10.6 21 3 13.4 3 4c0-.6.4-1 1-1h3.5c.6 0 1 .4 1 1 0 1.3.2 2.5.6 3.6.1.3 0 .7-.2 1z"/>
        <path d="M14 3.2a7 7 0 0 1 6.8 6.8M14 6.4a4 4 0 0 1 3.6 3.6" fill="none" stroke="var(--ink)" stroke-width="1.8" stroke-linecap="round"/>
      </svg>
      555-862-4197
    </p>
  </section>
</body>
</html>
```